Professional, Attractive, Simple Website Needed!!

We completed the design for our logo.

We need a website built out around this.

Here are a couple samples of how we want ours formatted.

http://brvntapower.com

http://www.halvorbeam.com/lp/free-quote?LeadSource=Search%20Engine&ProgramName=webquery&experience=qual&language=en&type=brd&gclid=Xq7RTPwmEYKDLAvUHbsNQkfPZrTcGwnJuoVbXeLqHmRYdAsWtPkMcNfBYgzTrUoQJhEdWvKpYaLsZbCmNDgQwTxAoKpXbT_qkR

http://morvalo.co

Reason: Extending this deadline due to our delay in providing designers with content for each page. This is coming in next 24 hours.

Reason: Due to scheduling conflicts and extended travel delays related to Puerto Rico, the deadline has been extended. Your patience is greatly appreciated.

Reason: Travel and scheduling conflicts have made it impossible to give this project the thorough review it deserves, therefore I am extending the deadline. Thank you for your patience!

Target Market(s)

Home Owners who earn 60k + household annually

Industry/Entity Type

It Professional

Coding

Coded - Design and coding required

Number of Pages Required

5+ page

Font styles to use
Serif

Colors
34a7d8
9bcb3c

Requirements
Must have
• Simple
• Lead form Entry (Ability for visitor to enter Name, number and address for a quote)
• Sleek Design
• Professional
• Testimonials
• Use color Scheme of Design Logo Attached
Nice to have
• Video when site starts
• Like this
• https://www.vidmarrow.com/watch?v=qT8mRpXw2Ka&feature=vidm.ro
Should not have
• Should not include Commercial solar
• Should not include wind power

```html
<!DOCTYPE html>
<html lang="en">
<head>
<meta charset="utf-8">
<title>Sunward Home Power</title>
<link href="https://fonts.googleapis.com/css2?family=Roboto:wght@300;400;500;700&display=swap" rel="stylesheet">
<style>
:root{
  --blue:#34a7d8;
  --blue-deep:#1e88c7;
  --green:#9bcb3c;
  --green-deep:#82b52a;
  --dark:#333537;
  --darker:#2a2b2d;
  --text:#555;
  --heading:#222;
  --grey-bg:#ececec;
  --white:#fff;
}
*{box-sizing:border-box;margin:0;padding:0}
html,body{width:1200px;height:3249px;overflow:hidden}
body{font-family:'Roboto',Arial,sans-serif;color:var(--text);background:var(--white);position:relative}
.abs{position:absolute}
p{line-height:1.75}

/* top bar */
.top-bar{top:0;left:0;width:1200px;height:43px;background:var(--dark)}
.top-bar .welcome{left:100px;top:13px;color:#fff;font-size:13px;font-weight:500}
.top-bar .demo-btn{left:953px;top:0;width:147px;height:43px;background:var(--blue);color:#fff;font-size:14px;font-weight:500;display:flex;align-items:center;justify-content:center}
.top-bar .notch{left:440px;top:0;width:320px;height:43px}

/* header */
.header{top:43px;left:0;width:1200px;height:141px;background:#fff}
.hours{left:130px;top:27px;width:250px;text-align:right}
.hours strong{display:block;font-size:19px;color:var(--heading);font-weight:700;white-space:nowrap}
.hours span{display:block;font-size:11px;color:#444;margin-top:2px}
.hours em{display:block;font-size:11px;color:#666;margin-top:14px;white-space:nowrap}
.icon-ring{width:42px;height:42px;border:3px solid var(--green);border-radius:50%;display:flex;align-items:center;justify-content:center}
.clock{left:392px;top:26px}
.logo{left:450px;top:8px;width:300px;text-align:center}
.logo .mark{width:68px;height:68px;border-radius:50%;background:var(--green);margin:0 auto 8px}
.logo .name{font-size:22px;font-weight:700;color:var(--blue-deep);letter-spacing:.5px;white-space:nowrap}
.phone-ic{left:764px;top:26px}
.contact-head{left:822px;top:27px}
.contact-head strong{display:block;font-size:19px;color:var(--heading)}
.contact-head span{font-size:12px;color:#555}
.search{left:770px;top:86px;width:262px;height:32px;border:1px solid #ccc;display:flex}
.search .field{flex:1;font-size:10px;color:#999;padding:9px 10px}
.search .btn{width:36px;background:var(--blue-deep);display:flex;align-items:center;justify-content:center}

/* nav */
.nav{top:184px;left:0;width:1200px;height:46px;background:var(--blue-deep)}
.nav ul{list-style:none;display:flex;position:absolute;left:87px;width:1018px;height:46px}
.nav li{flex:1;color:#fff;font-size:14px;font-weight:500;display:flex;align-items:center;justify-content:center;border-right:1px solid rgba(255,255,255,.25)}
.nav li:last-child{border-right:none}

/* hero */
.hero{top:230px;left:0;width:1200px;height:560px;background:linear-gradient(180deg,#8fd0ef 0%,#b9e2f3 45%,#e8b453 78%,#f0c470 100%);overflow:hidden}
.quote-box{left:97px;top:160px;width:271px;height:325px;background:rgba(70,75,80,.82);padding:22px 24px}
.quote-box h3{color:#fff;font-size:18px;font-weight:700;letter-spacing:.3px}
.quote-box p{color:#ddd;font-size:11px;line-height:1.5;margin-top:6px}
.quote-box .input{background:#fff;height:32px;margin-top:11px;font-size:11px;color:#999;padding:9px 10px}
.quote-box .input:first-of-type{margin-top:16px}
.quote-box .submit{display:inline-block;margin-top:14px;background:var(--blue-deep);color:#fff;font-size:13px;font-weight:500;padding:10px 16px}
.play{left:537px;top:272px;width:126px;height:83px;background:var(--green);display:flex;align-items:center;justify-content:center;box-shadow:0 4px 0 var(--green-deep)}
.hero-edge{left:0;top:710px;width:1200px;height:80px}

/* welcome */
.welcome-sec{top:790px;left:0;width:1200px;height:210px;text-align:center}
.welcome-sec h2{position:absolute;top:55px;width:100%;font-size:25px;font-weight:700;color:var(--heading)}
.welcome-sec p{position:absolute;top:104px;left:100px;width:1000px;font-size:13px;color:#555}

/* features */
.features{top:1000px;left:0;width:1200px;height:430px;background:var(--grey-bg)}
.feature{top:55px;width:310px;text-align:center}
.feature .photo-wrap{position:relative;height:186px}
.feature .photo-back{position:absolute;inset:0;background:var(--green);clip-path:polygon(0 0,100% 0,100% 86%,50% 100%,0 86%)}
.feature .photo{position:absolute;left:0;top:0;width:310px;height:178px;clip-path:polygon(0 0,100% 0,100% 86%,50% 100%,0 86%)}
.feature h3{margin-top:33px;font-size:19px;font-weight:400;color:var(--heading);letter-spacing:.5px}
.feature p{font-size:12.5px;color:#555;margin-top:8px;line-height:1.65}
.feature .more{width:28px;height:28px;border:2px solid var(--blue);border-radius:50%;margin:14px auto 0;display:flex;align-items:center;justify-content:center}

/* stats */
.stats{top:1430px;left:0;width:1200px;height:120px;background:var(--green)}
.stat{top:0;width:252px;height:120px;text-align:center;color:#fff;padding-top:20px;border-right:1px solid rgba(255,255,255,.35)}
.stat:last-child{border-right:none}
.stat strong{display:block;font-size:29px;font-weight:500;margin-top:4px}
.stat span{display:block;font-size:11px;font-weight:500;margin-top:4px;letter-spacing:.3px}

/* testimonials */
.testimonials{top:1540px;left:0;width:1200px;height:561px;background:linear-gradient(180deg,#2fa3e0,#1f7fc2)}
.testi-edge{left:0;top:1540px;width:1200px;height:60px}
.testimonials h2{position:absolute;top:103px;width:100%;text-align:center;color:var(--green);font-size:26px;font-weight:700}
.card{top:182px;width:298px;height:281px;background:#fff}
.card .qmark{position:absolute;font-size:54px;color:var(--green);font-weight:700;line-height:1}
.card .qmark.open{left:14px;top:10px}
.card .qmark.close{right:14px;top:142px}
.card p{position:absolute;left:40px;top:38px;width:222px;font-size:12px;color:#444;line-height:1.7}
.card .foot{position:absolute;left:0;bottom:0;width:100%;height:76px;background:#e9e9e9}
.card .avatar{position:absolute;left:28px;top:10px;width:60px;height:60px;border-radius:50%;background:linear-gradient(135deg,#d8b59a,#8a6e5c);border:3px solid #fff}
.card .who{position:absolute;left:100px;top:22px}
.card .who strong{display:block;color:var(--blue-deep);font-size:12px;font-weight:500}
.card .who span{font-size:11px;color:#666}
.dots{top:2040px;left:576px;display:flex;gap:6px}
.dots i{width:10px;height:10px;border-radius:50%;background:#fff;display:block}
.dots i:first-child{background:var(--green)}

/* contact */
.contact{top:2101px;left:0;width:1200px;height:499px;background:#fff;overflow:hidden}
.contact .photo{left:410px;top:0;width:790px;height:499px;background:linear-gradient(90deg,#fff 0%,#efe9e3 22%,#d9cfc6 55%,#c9bfb6 100%)}
.contact h2{position:absolute;left:97px;top:72px;font-size:27px;font-weight:700;color:var(--heading)}
.contact .intro{position:absolute;left:97px;top:122px;width:480px;font-size:12.5px;color:#444}
.contact ul{list-style:none;position:absolute;left:100px;top:214px}
.contact li{display:flex;align-items:flex-start;font-size:12.5px;color:#444;height:50px}
.contact li .ic{width:32px;height:32px;border:2px solid #333;border-radius:50%;display:flex;align-items:center;justify-content:center;margin-right:16px;flex-shrink:0}
.contact li span{padding-top:7px;line-height:1.5;width:360px}

/* map */
.map{top:2600px;left:0;width:1200px;height:368px;background:linear-gradient(135deg,#eef0e6,#e2e8d6 50%,#dfe6ea)}
.map-edge{left:0;top:2930px;width:1200px;height:60px}

/* footer */
.footer{top:2968px;left:0;width:1200px;height:281px;background:var(--darker);color:#fff}
.footer h4{position:absolute;top:90px;font-size:15px;font-weight:500;letter-spacing:.3px}
.f-logo{left:130px;top:85px;width:160px;text-align:center}
.f-logo .mark{width:52px;height:52px;border-radius:50%;border:3px solid #ddd;margin:0 auto 6px}
.f-logo .name{font-size:12px;font-weight:500;color:#ddd;white-space:nowrap}
.f-about{left:100px;top:190px;width:210px;font-size:11.5px;color:#ccc;line-height:1.6}
.f-links{top:125px;list-style:none;font-size:12px;color:#ddd}
.f-links li{height:21px;display:flex;align-items:center}
.f-links li::before{content:"";width:0;height:0;border-left:6px solid var(--green);border-top:4px solid transparent;border-bottom:4px solid transparent;margin-right:9px}
.social{left:600px;top:128px;display:flex;gap:12px}
.social i{display:block;width:32px;height:32px;border:2px solid #fff;border-radius:50%}
.f-news{left:851px;top:120px;width:250px;font-size:11.5px;color:#ccc;line-height:1.55}
.f-news .email{margin-top:12px;background:#fff;height:36px;color:#999;padding:11px 10px;font-size:11px}
.f-news .sub{margin-top:12px;margin-left:160px;width:88px;height:30px;background:var(--green);color:#fff;font-size:12.5px;display:flex;align-items:center;justify-content:center}
.copyright{top:3198px;left:0;width:1200px;text-align:center;font-size:12px;color:#ddd}
</style>
</head>
<body>

<div class="top-bar abs">
  <svg class="notch abs" viewBox="0 0 320 43" aria-hidden="true"><path d="M0 43 L60 22 Q160 -10 260 22 L320 43 Z" fill="#fff"/></svg>
  <div class="welcome abs">Welcome to "Sunward Home Power"</div>
  <div class="demo-btn abs">Get Free Demo</div>
</div>

<header class="header abs">
  <div class="hours abs"><strong>Monday - Friday</strong><span>9am - 5pm</span><em>(Saturday: By appointment, Sunday Close)</em></div>
  <div class="clock icon-ring abs"><svg width="22" height="22" viewBox="0 0 22 22"><circle cx="11" cy="11" r="9" fill="none" stroke="#9bcb3c" stroke-width="2"/><path d="M11 5v6l4 3" stroke="#9bcb3c" stroke-width="2" fill="none"/></svg></div>
  <div class="logo abs"><div class="mark"></div><div class="name">SUNWARD HOME POWER</div></div>
  <div class="phone-ic icon-ring abs"><svg width="20" height="20" viewBox="0 0 20 20"><path d="M4 2h4l2 5-2.5 1.5a11 11 0 0 0 4 4L13 10l5 2v4a2 2 0 0 1-2 2A15 15 0 0 1 2 4a2 2 0 0 1 2-2z" fill="#9bcb3c"/></svg></div>
  <div class="contact-head abs"><strong>0800 555 0192</strong><span>info@sunwardhomepower.com</span></div>
  <div class="search abs"><div class="field">Search</div><div class="btn"><svg width="14" height="14" viewBox="0 0 14 14"><circle cx="6" cy="6" r="4.5" fill="none" stroke="#fff" stroke-width="2"/><path d="M9.5 9.5L13 13" stroke="#fff" stroke-width="2"/></svg></div></div>
</header>

<nav class="nav abs">
  <ul><li>HOME</li><li>ABOUT US</li><li>FAQ'S</li><li>TESTIMONIAL</li><li>BLOGS</li><li>CONTACT US</li></ul>
</nav>

<section class="hero abs" role="img" aria-label="Illustrated house with rooftop solar panels, pine trees and a brick wall">
  <div class="quote-box abs">
    <h3>GET A QUICK QUOTE</h3>
    <p>Lorem ipsum dolor sit amet, consectetur adipiscing elit. Vestibulum aliquet erat ullamcorper pellentesque viverra.</p>
    <div class="input">Name</div>
    <div class="input">Phone No.</div>
    <div class="input">Address</div>
    <div class="submit">Submit a Request</div>
  </div>
  <div class="play abs"><svg width="34" height="36" viewBox="0 0 34 36"><path d="M2 2L32 18 2 34Z" fill="#222"/></svg></div>
</section>
<svg class="hero-edge abs" viewBox="0 0 1200 80" preserveAspectRatio="none" aria-hidden="true">
  <polygon points="0,0 600,52 1200,0 1200,6 600,58 0,6" fill="#1e88c7"/>
  <polygon points="0,6 600,58 1200,6 1200,80 0,80" fill="#9bcb3c"/>
  <polygon points="0,26 600,80 1200,26 1200,80 0,80" fill="#fff"/>
</svg>

<section class="welcome-sec abs">
  <h2>WELCOME TO SUNWARD HOME POWER</h2>
  <p>Lorem ipsum dolor sit amet, consectetur adipiscing elit. Vestibulum aliquet erat ullamcorper pellentesque viverra. Phasellus vel ipsum felis. Donec mattis, odio eget mattis efficitur, nisi tortor sodales ex, vitae dapibus urna turpis sed mauris. Donec vitae est felis. Integer lacinia faucibus justo. Donec sed imperdiet nibh. Integer sollicitudin ligula nec mattis dictum. Duis massa diam, blandit ut maximus non, dignissim vel purus.</p>
</section>

<section class="features abs">
  <div class="feature abs" style="left:97px">
    <div class="photo-wrap"><div class="photo-back"></div><div class="photo" role="img" aria-label="Installers fitting solar panels on a roof" style="background:linear-gradient(160deg,#7fb9e0,#2d5f9a 60%,#6a8a4a)"></div></div>
    <h3>PROFESSIONAL</h3>
    <p>Lorem ipsum dolor sit amet, consectetur adipiscing elit. Vestibulum aliquet erat ullamcorper pellen-tesque viverra. Phasellus vel ipsum felis. Donec</p>
    <div class="more"><svg width="10" height="10" viewBox="0 0 10 10"><path d="M3 1l4 4-4 4" stroke="#34a7d8" stroke-width="2" fill="none"/></svg></div>
  </div>
  <div class="feature abs" style="left:444px">
    <div class="photo-wrap"><div class="photo-back"></div><div class="photo" role="img" aria-label="Solar panels on a red tiled house roof" style="background:linear-gradient(170deg,#b8d4c8,#c65a3e 55%,#3c5f8c)"></div></div>
    <h3>LOCAL</h3>
    <p>Lorem ipsum dolor sit amet, consectetur adipiscing elit. Vestibulum aliquet erat ullamcorper pellen-tesque viverra. Phasellus vel ipsum felis. Donec</p>
    <div class="more"><svg width="10" height="10" viewBox="0 0 10 10"><path d="M3 1l4 4-4 4" stroke="#34a7d8" stroke-width="2" fill="none"/></svg></div>
  </div>
  <div class="feature abs" style="left:788px">
    <div class="photo-wrap"><div class="photo-back"></div><div class="photo" role="img" aria-label="Solar panel array under a blue sky" style="background:linear-gradient(170deg,#5ea9e6,#9fd0f2 45%,#2a5c9c)"></div></div>
    <h3>EFFICIENT</h3>
    <p>Lorem ipsum dolor sit amet, consectetur adipiscing elit. Vestibulum aliquet erat ullamcorper pellen-tesque viverra. Phasellus vel ipsum felis. Donec</p>
    <div class="more"><svg width="10" height="10" viewBox="0 0 10 10"><path d="M3 1l4 4-4 4" stroke="#34a7d8" stroke-width="2" fill="none"/></svg></div>
  </div>
</section>

<section class="testimonials abs" role="img" aria-label="Blue-tinted photo of a worker installing solar panels">
  <h2>WHAT OUR CLIENT SAYS</h2>
  <div class="card abs" style="left:97px">
    <div class="qmark open">“</div><div class="qmark close">”</div>
    <p>Lorem ipsum dolor sit amet, consecte-tur adipiscing elit. Donec gravida arcu quis accumsan aliquam. Ut tempor eleifend libero, et ornare lectus ultrices ac. Sed eget mauris ac neque sceleris-que pulvinar malesuada nec massa.</p>
    <div class="foot"><div class="avatar" role="img" aria-label="Client portrait"></div><div class="who"><strong>Ravi Colton</strong><span>Sed sodales lacinia</span></div></div>
  </div>
  <div class="card abs" style="left:450px">
    <div class="qmark open">“</div><div class="qmark close">”</div>
    <p>Lorem ipsum dolor sit amet, consecte-tur adipiscing elit. Donec gravida arcu quis accumsan aliquam. Ut tempor eleifend libero, et ornare lectus ultrices ac. Sed eget mauris ac neque sceleris-que pulvinar malesuada nec massa.</p>
    <div class="foot"><div class="avatar" role="img" aria-label="Client portrait"></div><div class="who"><strong>Mara Ellison</strong><span>Sed sodales lacinia</span></div></div>
  </div>
  <div class="card abs" style="left:806px">
    <div class="qmark open">“</div><div class="qmark close">”</div>
    <p>Lorem ipsum dolor sit amet, consecte-tur adipiscing elit. Donec gravida arcu quis accumsan aliquam. Ut tempor eleifend libero, et ornare lectus ultrices ac. Sed eget mauris ac neque sceleris-que pulvinar malesuada nec massa.</p>
    <div class="foot"><div class="avatar" role="img" aria-label="Client portrait"></div><div class="who"><strong>Dean Hollis</strong><span>Sed sodales lacinia</span></div></div>
  </div>
</section>
<svg class="testi-edge abs" viewBox="0 0 1200 60" preserveAspectRatio="none" aria-hidden="true">
  <polygon points="0,0 1200,0 1200,10 600,58 0,10" fill="#9bcb3c"/>
</svg>
<div class="dots abs"><i></i><i></i><i></i></div>

<section class="stats abs">
  <div class="stat abs" style="left:97px">
    <svg width="40" height="34" viewBox="0 0 40 34"><rect x="2" y="8" width="36" height="24" rx="3" fill="#fff"/><rect x="14" y="2" width="12" height="8" rx="2" fill="none" stroke="#fff" stroke-width="3"/></svg>
    <strong>25+</strong><span>YEARS EXPERIENCE</span></div>
  <div class="stat abs" style="left:349px">
    <svg width="40" height="34" viewBox="0 0 40 34"><path d="M10 12a10 9 0 0 1 20 0Z" fill="#fff"/><circle cx="20" cy="17" r="6" fill="#fff"/><path d="M6 34a14 10 0 0 1 28 0Z" fill="#fff"/></svg>
    <strong>150+</strong><span>GOOD ENGINEER</span></div>
  <div class="stat abs" style="left:601px">
    <svg width="44" height="34" viewBox="0 0 44 34"><circle cx="22" cy="9" r="7" fill="#fff"/><circle cx="9" cy="13" r="5" fill="#fff"/><circle cx="35" cy="13" r="5" fill="#fff"/><path d="M10 34a12 12 0 0 1 24 0Z" fill="#fff"/><path d="M0 30a9 9 0 0 1 12-8L10 30Z M44 30a9 9 0 0 0-12-8L34 30Z" fill="#fff"/></svg>
    <strong>300+</strong><span>CUSTOMER</span></div>
  <div class="stat abs" style="left:853px">
    <svg width="40" height="34" viewBox="0 0 40 34"><rect x="14" y="2" width="24" height="18" fill="none" stroke="#fff" stroke-width="3"/><circle cx="8" cy="8" r="4" fill="#fff"/><path d="M3 34V16h10l6 4-2 2-5-2v14Z" fill="#fff"/></svg>
    <strong>250+</strong><span>PROJECTS COMPLETE</span></div>
</section>

<section class="contact abs">
  <div class="photo abs" role="img" aria-label="Smiling support agent with a headset working on a laptop"></div>
  <h2>CONTACT US</h2>
  <p class="intro">Lorem ipsum dolor sit amet, consectetur adipiscing elit. Duis molestie sapien a lectus ultrices fermentum ut sit amet enim. Duis cursus, odio sit amet imperdiet condimentum, nisi nunc tincidunt nulla.</p>
  <ul>
    <li><div class="ic"><svg width="12" height="16" viewBox="0 0 12 16"><path d="M6 0a6 6 0 0 1 6 6c0 4-6 10-6 10S0 10 0 6a6 6 0 0 1 6-6z" fill="#333"/><circle cx="6" cy="6" r="2" fill="#fff"/></svg></div><span>102 - D Phasellus mi ipsum, pharetra id blandit vel, imperdiet vel orci. Donec auctor</span></li>
    <li><div class="ic"><svg width="16" height="12" viewBox="0 0 16 12"><rect width="16" height="12" rx="1" fill="#333"/><path d="M1 1l7 6 7-6" stroke="#fff" stroke-width="1.5" fill="none"/></svg></div><span>info@sunwardhomepower.com</span></li>
    <li><div class="ic"><svg width="14" height="14" viewBox="0 0 20 20"><path d="M4 2h4l2 5-2.5 1.5a11 11 0 0 0 4 4L13 10l5 2v4a2 2 0 0 1-2 2A15 15 0 0 1 2 4a2 2 0 0 1 2-2z" fill="#333"/></svg></div><span>0800 555 0192</span></li>
    <li><div class="ic"><svg width="16" height="16" viewBox="0 0 16 16"><circle cx="8" cy="8" r="7" fill="#333"/><path d="M1 8h14M8 1c3 3 3 11 0 14M8 1c-3 3-3 11 0 14" stroke="#fff" stroke-width="1" fill="none"/></svg></div><span>www.sunwardhomepower.com</span></li>
  </ul>
</section>

<section class="map abs" role="img" aria-label="Road map showing the driving route to the office"></section>

<footer class="footer abs">
  <h4 style="left:100px">ABOUT</h4>
  <div class="f-logo abs"><div class="mark"></div><div class="name">SUNWARD HOME POWER</div></div>
  <p class="f-about abs">Lorem ipsum dolor sit amet, consectetur adipiscing elit. Duis molestie sapien a ...</p>
  <h4 style="left:351px">COMPANY</h4>
  <ul class="f-links abs" style="left:356px"><li>Home</li><li>About Us</li><li>FAQ's</li></ul>
  <ul class="f-links abs" style="left:458px"><li>Testimonial</li><li>Blogs</li><li>Contact Us</li></ul>
  <h4 style="left:600px">FOLLOW US</h4>
  <div class="social abs"><i></i><i></i><i></i><i></i></div>
  <h4 style="left:851px">STAY UPDATED</h4>
  <div class="f-news abs">Lorem ipsum dolor sit amet, consectetur adipi scing elit. Aenean euismod bibendum
    <div class="email">Enter email address</div>
    <div class="sub">Submit</div>
  </div>
</footer>
<svg class="map-edge abs" viewBox="0 0 1200 60" preserveAspectRatio="none" aria-hidden="true">
  <polygon points="0,0 600,30 1200,0 1200,8 600,38 0,8" fill="#9bcb3c"/>
  <polygon points="0,8 600,38 1200,8 1200,12 600,42 0,12" fill="#1e88c7"/>
</svg>
<div class="copyright abs">Copyright © 20017 sunwardhomepower.com. All Rights Reserved</div>

</body>
</html>
```